Need design for an App.

The app in question is related to security and crime events with real time feed, engagement with friends and posting pictures, we want a sleak, minimal style. There are 11 or 12 screens to be made. We are adding video file as suggestion. We are not sure about colors so we accept suggestions. We are also adding the logo.

Reason: Just giving more time to designers. Thanks.

Industry/Entity Type

Security

Font styles to use
Sans Serif

Requirements
Must have
• The app must have a Login view; a new user view (with nickname, email and pass); a retrieve pass view; a menu view with options for alert configuration, send emergency alert and send report, a feed view with the most popular reports (3 worldwide at the top and near reports after), a profile view with avatar and personal reports, a send emergency alert view with a camera view; a configuration view when the user can put up to 5 contacts to send the alert to them;a send report view with camera and options to configure the camera; a edit report view where the user can see the 3 photos he will update and add a comment of those photos.
Nice to have
• Check the files we are open minds
Should not have
• old design

```html
<!DOCTYPE html>
<html lang="en">
<head>
<meta charset="utf-8">
<title>Sentral – Home Menu</title>
<link rel="stylesheet" href="https://fonts.googleapis.com/css2?family=Roboto+Condensed:ital,wght@0,300;0,400;0,700;1,300;1,400&display=swap">
<style>
  :root {
    --brand-red: #c61a3d;
    --brand-red-dark: #a8142f;
    --ink-white: #ffffff;
    --bar-black: #000000;
    --city-dark: #141414;
    --city-mid: #2b2b2b;
    --dot-muted: rgba(255,255,255,0.55);
  }
  * { box-sizing: border-box; margin: 0; padding: 0; }
  html, body {
    width: 1200px; height: 2456px; overflow: hidden;
    background: var(--city-dark);
    font-family: "Roboto Condensed", "Arial Narrow", sans-serif;
    color: var(--ink-white);
  }
  .screen { position: relative; width: 1200px; height: 2456px; overflow: hidden; }

  .backdrop {
    position: absolute; inset: 0;
    background: radial-gradient(ellipse at 55% 55%, var(--city-mid) 0%, #1c1c1c 45%, var(--city-dark) 100%);
  }

  .status-bar {
    position: absolute; top: 0; left: 0; width: 100%; height: 90px;
    background: var(--bar-black);
    display: flex; align-items: center; justify-content: space-between;
    padding: 0 34px; font-size: 40px; font-weight: 400;
  }
  .status-left, .status-right { display: flex; align-items: center; gap: 16px; }
  .signal-dots { display: flex; gap: 6px; }
  .signal-dots span { width: 18px; height: 18px; border-radius: 50%; background: var(--ink-white); }

  .menu-panel {
    position: absolute; top: 90px; left: 0; width: 100%; height: 1370px;
    background: var(--brand-red);
    border-radius: 0 0 90px 90px;
  }
  .app-header {
    height: 110px; display: flex; align-items: center; justify-content: space-between;
    padding: 0 30px; border-bottom: 5px solid var(--ink-white);
  }
  .hamburger { display: flex; flex-direction: column; gap: 12px; }
  .hamburger span { width: 82px; height: 11px; background: var(--ink-white); border-radius: 2px; }
  .header-badge {
    width: 62px; height: 62px; border-radius: 50%;
    border: 7px solid var(--ink-white); margin-right: 14px;
  }

  .profile-block { text-align: center; padding-top: 60px; }
  .profile-block svg { display: block; margin: 0 auto; }
  .tagline {
    margin: 36px auto 0; width: 980px;
    font-style: italic; font-weight: 300; font-size: 46px; line-height: 1.25;
  }
  .pager-dots { display: flex; justify-content: center; gap: 8px; margin-top: 18px; }
  .pager-dots span { width: 8px; height: 8px; border-radius: 50%; background: var(--dot-muted); }

  .divider { height: 5px; background: var(--ink-white); margin-top: 14px; }

  .action-grid {
    display: grid; grid-template-columns: repeat(4, 1fr);
    padding: 50px 20px 0; text-align: center;
  }
  .action svg { display: block; margin: 0 auto; }
  .action-label { margin-top: 30px; font-size: 32px; font-weight: 400; white-space: nowrap; }

  .panel-dots { position: absolute; bottom: 54px; left: 0; width: 100%; }

  .copyright {
    position: absolute; bottom: 96px; width: 100%; text-align: center;
    font-size: 31px; letter-spacing: 1px; font-weight: 400;
  }
</style>
</head>
<body>
<main class="screen">
  <div class="backdrop" role="img" aria-label="Dark, blurred city street photograph behind the menu"></div>

  <header class="status-bar">
    <div class="status-left">
      <div class="signal-dots"><span></span><span></span><span></span><span></span><span></span></div>
      <span>Amberline</span>
      <svg width="44" height="34" viewBox="0 0 44 34"><path d="M22 30 L28 23 A9 9 0 0 0 16 23 Z" fill="#fff"/><path d="M8 15 A20 20 0 0 1 36 15" stroke="#fff" stroke-width="5" fill="none"/><path d="M2 8 A29 29 0 0 1 42 8" stroke="#fff" stroke-width="5" fill="none"/></svg>
    </div>
    <div class="status-right">
      <svg width="22" height="38" viewBox="0 0 22 38"><path d="M3 10 L19 27 L11 35 V3 L19 11 L3 28" stroke="#fff" stroke-width="3" fill="none"/></svg>
      <span>82%</span>
      <svg width="80" height="36" viewBox="0 0 80 36"><rect x="2" y="2" width="68" height="32" rx="5" stroke="#fff" stroke-width="3" fill="none"/><rect x="7" y="7" width="50" height="22" fill="#fff"/><rect x="72" y="12" width="5" height="12" fill="#fff"/></svg>
    </div>
  </header>

  <section class="menu-panel">
    <div class="app-header">
      <div class="hamburger" aria-label="Menu"><span></span><span></span><span></span></div>
      <div class="header-badge" aria-label="Sentral"></div>
    </div>

    <div class="profile-block">
      <svg width="250" height="250" viewBox="0 0 250 250" aria-label="User avatar">
        <circle cx="125" cy="125" r="112" stroke="#fff" stroke-width="16" fill="none"/>
        <clipPath id="avatar-clip"><circle cx="125" cy="125" r="96"/></clipPath>
        <g clip-path="url(#avatar-clip)" fill="#fff">
          <circle cx="125" cy="95" r="40"/>
          <path d="M45 230 Q50 150 125 148 Q200 150 205 230 Z"/>
        </g>
        <path d="M113 150 L137 150 L131 162 L138 200 L125 212 L112 200 L119 162 Z" fill="var(--brand-red)"/>
      </svg>
      <p class="tagline">Lorem Ipsum is simply dummy text of the printing and typesetting industry.</p>
      <div class="pager-dots"><span></span><span></span><span></span></div>
    </div>

    <div class="divider"></div>

    <nav class="action-grid">
      <div class="action">
        <svg width="190" height="190" viewBox="0 0 190 190">
          <circle cx="95" cy="95" r="84" stroke="#fff" stroke-width="14" fill="none" stroke-dasharray="110 22"/>
          <g fill="#fff"><rect x="48" y="80" width="22" height="34" rx="3"/><path d="M70 80 L120 56 V138 L70 114 Z"/><rect x="60" y="114" width="16" height="30" rx="3"/></g>
          <g stroke="#fff" stroke-width="6" stroke-linecap="round"><path d="M132 97 H150"/><path d="M130 74 L145 64"/><path d="M130 120 L145 130"/></g>
        </svg>
        <p class="action-label">Emergency Alert</p>
      </div>
      <div class="action">
        <svg width="190" height="190" viewBox="0 0 190 190">
          <circle cx="95" cy="95" r="84" stroke="#fff" stroke-width="14" fill="none" stroke-dasharray="110 22"/>
          <g fill="#fff"><circle cx="112" cy="72" r="20"/><path d="M78 134 Q80 98 112 96 Q144 98 146 134 Z"/><circle cx="76" cy="84" r="16"/><path d="M46 136 Q48 108 76 106 Q90 107 96 114 Q84 122 82 136 Z"/></g>
        </svg>
        <p class="action-label">Send Report</p>
      </div>
      <div class="action">
        <svg width="190" height="190" viewBox="0 0 190 190">
          <circle cx="95" cy="95" r="84" stroke="#fff" stroke-width="14" fill="none" stroke-dasharray="110 22"/>
          <circle cx="95" cy="95" r="52" stroke="#fff" stroke-width="10" fill="none"/>
          <g fill="#fff"><path d="M87 64 H103 L100 108 H90 Z"/><circle cx="95" cy="124" r="8"/></g>
        </svg>
        <p class="action-label">Alert Configuration</p>
      </div>
      <div class="action">
        <svg width="190" height="190" viewBox="0 0 190 190">
          <circle cx="95" cy="95" r="84" stroke="#fff" stroke-width="14" fill="none" stroke-dasharray="110 22"/>
          <circle cx="95" cy="95" r="54" fill="#fff"/>
          <g fill="var(--brand-red)"><circle cx="95" cy="95" r="20"/>
            <path d="M95 45 L102 75 L88 75 Z" transform="rotate(0 95 95)"/>
            <path d="M95 45 L102 75 L88 75 Z" transform="rotate(60 95 95)"/>
            <path d="M95 45 L102 75 L88 75 Z" transform="rotate(120 95 95)"/>
            <path d="M95 45 L102 75 L88 75 Z" transform="rotate(180 95 95)"/>
            <path d="M95 45 L102 75 L88 75 Z" transform="rotate(240 95 95)"/>
            <path d="M95 45 L102 75 L88 75 Z" transform="rotate(300 95 95)"/>
          </g>
        </svg>
        <p class="action-label">Camera Alert</p>
      </div>
    </nav>

    <div class="pager-dots panel-dots"><span></span><span></span><span></span></div>
  </section>

  <footer class="copyright">COPYRIGHT ©2014 SENTRAL. ALL RIGHTS RESERVED</footer>
</main>
</body>
</html>
```